Counting Toward Purpose institute for nonprofits needs brochure

The Counting Toward Purpose performance management institute helps nonprofits clarify the intended impact of their programs on clients. What does a nonprofit want to accomplish - and what does it need to measure so that it can tell if they've achieved impact? The Institute is about to recruit participanting organizations. We have a lot of wording on a 2 page "flyer" that describes the institute...but it is a very ugly piece that looks unprofessional. We are looking for designs that are consistent with the KRT Advisory Group look (see our website). We are aware that we may have too much wording.

Target Market(s)

Nonprofit organization Executive Directors

Industry/Entity Type

Non-Profit

Font styles to use
Sans Serif

Requirements
Must have
• Must be able to be emailed to a client and printed on 8.5x11 paper. Doesn't matter to me if that makes it a tri-fold or two-fold.
• Need to be able to drop in later the actual dates of the program.
• Go to our website to see how we present ourselves. www.krtadvisoryhub.example
Nice to have
• See our website for KRT Advisory's "look". Our colors are green and gray (in the logo), with complementary colors of blue and orange.
• Looking for creativity in the graphics design. Our two page document has way too many words. The word impact is very important to the concept of performance management (and I'm not sure it's in the 2 page write up) - so you could do something with that word if you wanted to.
• Could use Davina's pic if it makes sense.
Should not have
• No new logo for the Counting Toward Purpose institute. It should be clear that KRT Advisory Group is the entity that offers the institute.

```html
<!DOCTYPE html>
<html lang="en">
<head>
<meta charset="utf-8">
<title>Counting Toward Purpose — Institute Brochure</title>
<link href="https://fonts.googleapis.com/css2?family=Mulish:ital,wght@0,400;0,700;0,800;0,900;1,400;1,800&family=Arimo:ital,wght@0,400;0,700;1,400&display=swap" rel="stylesheet">
<style>
  :root{
    --green:#86dc12;
    --blue:#3db6ee;
    --gold:#ddab00;
    --gray:#7d878b;
    --ink:#111;
    --rule:#8a8f91;
    --tint:#f5f6f6;
    --bg:#eeefef;
  }
  *{box-sizing:border-box;margin:0;padding:0}
  html,body{width:1200px;height:1200px;overflow:hidden;background:var(--bg)}
  body{font-family:"Arimo",Arial,sans-serif;color:var(--ink);position:relative}
  .spread{position:absolute;left:25px;top:152px;width:1150px;height:895px;background:#fff}
  .spread>*{position:absolute}
  .fold{left:570px;top:0;width:1px;height:895px;background:#e4e6e6}
  h2{font-family:"Mulish",sans-serif;font-weight:900;font-size:29px;letter-spacing:.2px;line-height:1}
  .green{color:var(--green)} .blue{color:var(--blue)} .gold{color:var(--gold)}
  .subtitle{left:27px;top:66px;width:460px;font-family:"Mulish",sans-serif;font-style:italic;font-size:22px;line-height:25px;color:var(--gray)}
  .intro-list{list-style:none;font-size:14px;line-height:17.5px}
  .intro-list li{position:relative;padding-left:26px;margin-bottom:20px}
  .intro-list li::before{content:"";position:absolute;left:3px;top:6px;width:6px;height:6px;border-radius:50%;background:var(--ink)}
  .intro-list b{display:block;font-family:"Mulish",sans-serif;font-weight:900;font-size:16.5px;line-height:19px}
  .body-copy{font-size:14px;line-height:17.5px}
  .goal{font-family:"Mulish",sans-serif;font-weight:900;font-style:italic;font-size:16.5px;line-height:23px}
  .pullquote{left:293px;top:392px;width:277px;height:290px;background:var(--tint);padding:20px 14px 0 19px}
  .pullquote .cap{float:left;font-family:"Mulish",sans-serif;font-weight:900;font-size:88px;line-height:66px;color:var(--gold);margin:4px 12px 0 0}
  .pullquote p{font-family:"Mulish",sans-serif;font-style:italic;font-size:19.5px;line-height:24.7px}
  .pullquote cite{display:block;margin-top:18px;font-family:"Mulish",sans-serif;font-style:normal;font-weight:900;font-size:15.5px;color:var(--gold)}
  .deliverables{left:27px;top:778px;width:530px;list-style:none;font-size:14px;line-height:17.5px}
  .deliverables li{position:relative;padding-left:26px;margin-bottom:8px}
  .deliverables li::before{content:"";position:absolute;left:3px;top:6px;width:5px;height:5px;border-radius:50%;background:var(--ink)}
  table.schedule{left:598px;top:167px;width:526px;border-collapse:collapse;font-family:"Mulish",sans-serif;font-size:12px;line-height:15px}
  .schedule th{background:var(--green);color:#fff;font-weight:800;font-size:14.5px;height:26px;border:1px solid var(--rule);letter-spacing:.3px}
  .schedule td{border:1px solid var(--rule);padding:0 5px;vertical-align:middle}
  .schedule td.when{font-style:italic}
  .schedule td.when span{font-style:italic}
  .note{left:598px;top:553px;font-size:11px}
  .comment{font-size:14px;line-height:17.5px}
  .comment em{font-style:normal;font-family:"Mulish",sans-serif;font-weight:800}
  .bubble{background:var(--tint);border-radius:30px}
</style>
</head>
<body>
<main class="spread">
  <div class="fold"></div>

  <h2 class="green" style="left:27px;top:32px">What is Performance Management</h2>
  <p class="subtitle">and why should nonprofits improve their performance management system?</p>

  <ul class="intro-list" style="left:27px;top:153px;width:255px">
    <li><b>High performance within</b>nonprofits is necessary because outcomes matter – to service consumers, staff, Board members, funders, and the community.</li>
    <li><b>Managing to outcomes</b>supports sound strategic decision-making, planning, and business development.</li>
  </ul>
  <ul class="intro-list" style="left:294px;top:153px;width:262px">
    <li><b>Performance management</b>is a process that provides agencies with the ability to manage to outcomes. &nbsp;Managing to outcomes is NOT a knee-jerk reaction to funder requirements but, instead, is mission-driven and provides a way to demonstrate the impact of the agency’s service delivery model.</li>
  </ul>

  <p class="body-copy" style="left:27px;top:351px;width:250px">Several agencies will participate in the institute; each will focus on one program’s performance management processes. Organizations develop systems at different speeds; the program is designed to accommodate this, with individually designed consultations for each participating agency.</p>
  <p class="goal" style="left:27px;top:518px;width:255px">The goal is that each agency will develop a culture and practices around performance management.</p>
  <p class="body-copy" style="left:27px;top:618px;width:255px">Up to four individuals will consistently participate from each agency, creating a team of performance management and implementation experts within the agency.</p>

  <aside class="pullquote">
    <span class="cap">H</span>
    <p>igh performance is the ability to deliver – over a prolonged period of time – meaningful, measurable, and financially sustainable results for the people or causes the organization is in existence to serve.</p>
    <cite>–Impact Framework</cite>
  </aside>

  <h2 class="blue" style="left:27px;top:730px">Project Deliverables</h2>
  <ul class="deliverables">
    <li>A plan that includes performance management systems for one program, and an action plan to develop a system for remaining programs.</li>
    <li>A culture of performance management, including a commitment to high quality program planning, implementation, evaluation and quality improvement, led by a staff team.</li>
  </ul>

  <h2 class="gold" style="left:598px;top:32px">Institute Cost</h2>
  <p class="body-copy" style="left:598px;top:78px">The 2017 Institute is offered at $10,000 per agency.</p>

  <h2 class="green" style="left:598px;top:118px">Institute Schedule</h2>
  <table class="schedule">
    <colgroup><col style="width:117px"><col style="width:161px"><col style="width:132px"><col style="width:116px"></colgroup>
    <thead><tr><th>FORMAT</th><th>TOPIC</th><th>DATE &amp; TIME</th><th>LOCATION</th></tr></thead>
    <tbody>
      <tr style="height:41px"><td>Consultation 1</td><td>Pre-assessment</td><td class="when">Need to be able to input</td><td>Agency</td></tr>
      <tr style="height:41px"><td>Session 1</td><td>What’s your <b>impact</b>?</td><td class="when">Date<br>8:30 AM - 12:30 PM</td><td>Elm Hollow Visitors Center*</td></tr>
      <tr style="height:23px"><td>Consultation 2</td><td>Individually paced</td><td class="when">Date</td><td>Agency</td></tr>
      <tr style="height:43px"><td>Session 2</td><td>What <b>outcomes</b> can you and should you measure?</td><td class="when">Date<br>8:30 AM - 12:30 PM</td><td>Elm Hollow Visitors Center</td></tr>
      <tr style="height:56px"><td>Session 3</td><td>What <b>processes</b> can you and should you measure?</td><td class="when">Date<br>8:30 AM - 12:30 PM</td><td>Elm Hollow Visitors Center</td></tr>
      <tr style="height:25px"><td>Consultation 3</td><td>Individually paced</td><td class="when">Date</td><td>Agency</td></tr>
      <tr style="height:25px"><td>Consultation 4</td><td>Individually paced</td><td class="when">Date</td><td>Agency</td></tr>
      <tr style="height:56px"><td>Session 4</td><td>What else can you and should you do with <b>the results</b>?</td><td class="when">Date<br>8:30 AM - 12:30 PM</td><td>Elm Hollow Visitors Center</td></tr>
      <tr style="height:41px"><td>Consultation 5</td><td>Action planning and post-assessment</td><td class="when">Date</td><td>Agency</td></tr>
    </tbody>
  </table>
  <p class="note">*Location tentative and will be confirmed in advance of Session 1</p>

  <h2 class="blue" style="left:598px;top:592px">Comments from Prior Participants</h2>
  <p class="comment bubble" style="left:657px;top:633px;width:466px;height:62px;padding:4px 16px 0 20px;text-align:right">“The content was extremely relevant and well planned. It felt like it was at <em class="blue">‘the right level’</em> for agencies that are in a variety of places with their performance management.”</p>
  <p class="comment" style="left:598px;top:708px;width:526px;text-align:center">“What I loved most about the Institute was the combination of <em class="green">one-on-one sessions</em> between our agency and the KRT team paired with the group sessions where <em class="green">we could learn from and collaborate with other agencies</em>.”</p>
  <p class="comment bubble" style="left:598px;top:771px;width:452px;height:50px;padding:7px 16px 0 17px">“If your agency is ready to learn how to best measure its data, then <em class="blue">absolutely consider the Institute</em>.”</p>
  <p class="comment" style="left:598px;top:831px;width:526px;text-align:center">“If you thought you knew about outcome measurement, you will leave the Institute <em class="gold">knowing more and being able to use it</em>!!”</p>
</main>
</body>
</html>
```